A specialised Sport management needs a corporate brochure design

We are a specialized company in the management and consultancy of sports events. and need to have a company brochure
We provide the following services;
Event management
Venues management
Production
Ticketing
Consulting
Hospitality
Activity management
Event timing
Branding of event
Event supplies
We need a corporate profile design for our company to showcase the major events that we have covered , with images, information, statistics, surveys, products and services used. We want to highlight our professionalism and execution of the events, experience of the participants, spectators . How we have grown in the past few years and reached the international standards.
Objectives of the work:
To get sponsors and partners for future business and to present Keel-Marrow
as not just a sports management company but also a professional sports
events management company.
You can check our website
www.keel-marrow.example
Target Market(s)
Sponsors and corporate partners
Industry/Entity Type
Events
Font styles to use
Requirements
Must have
- Must Have:
- - Very professional look
- -Some event images,Event information, statistics, surveys, products and services used. We want to highlight our professionalism and execution of the events (Attached)
Nice to have
- Similar momentom of the below design
- http://www.dunlathgames.example/wp-content/themes/dunlath_games/pdf/CP-2014-15-V10-Web.pdf

```html
<!DOCTYPE html>
<html lang="en">
<head>
<meta charset="utf-8">
<title>Keel-Marrow Brochure – Marketing Spread</title>
<link href="https://fonts.googleapis.com/css2?family=Orbitron:wght@500;700&family=Arimo:wght@400;700&display=swap" rel="stylesheet">
<style>
  :root {
    --bg: #dcdcdc;
    --paper: #eeedeb;
    --paper-shade: #e4e3e0;
    --orange: #ee5a2a;
    --ink: #2b2b2b;
    --grey: #8a8a8c;
    --grey-dark: #6d6d70;
    --green: #2c9b4e;
    --rule: #e9a58c;
  }
  * { box-sizing: border-box; margin: 0; padding: 0; }
  html, body { width: 1200px; height: 799px; overflow: hidden; background: var(--bg); }
  body { position: relative; font-family: "Arimo", Arial, sans-serif; color: var(--ink); }

  .spread {
    position: absolute; left: 50px; top: 120px; width: 1100px; height: 560px;
    display: flex; box-shadow: 0 10px 30px rgba(0,0,0,.18);
  }
  .page { position: relative; width: 550px; height: 560px; background: var(--paper); overflow: hidden; }
  .page--left { background: linear-gradient(to right, var(--paper) 88%, var(--paper-shade)); }
  .page--right { background: linear-gradient(to left, var(--paper) 90%, var(--paper-shade)); }

  .folio-tab { position: absolute; width: 16px; height: 6px; background: var(--green); }
  .page--left .folio-tab { left: 0; top: 400px; }
  .page--right .folio-tab { right: 40px; top: 150px; }

  /* Left page */
  .section-title {
    position: absolute; left: 36px; top: 262px;
    font-family: "Orbitron", sans-serif; font-weight: 700; font-size: 33px;
    letter-spacing: 1px; color: var(--orange); white-space: nowrap;
  }
  .copy-column {
    position: absolute; left: 36px; top: 318px; width: 262px;
    display: flex; flex-direction: column; gap: 16px;
    font-size: 11px; line-height: 1.45;
  }
  .copy h3 { font-size: 11.5px; font-weight: 700; margin-bottom: 3px; }

  .stat { position: absolute; font-size: 9px; line-height: 1.25; color: var(--ink); white-space: nowrap; }
  .stat-figure {
    display: block; font-family: "Orbitron", sans-serif; font-weight: 500;
    font-size: 24px; color: var(--orange); line-height: 1.05; letter-spacing: 1px;
  }
  .stat-figure sup { font-size: 10px; vertical-align: top; }
  .stat-figure small { font-size: 8px; letter-spacing: .5px; }
  .stat--impressions { left: 322px; top: 226px; }
  .stat--comments { left: 440px; top: 200px; }
  .stat--contributors { left: 325px; top: 336px; }
  .stat--posts { left: 455px; top: 330px; }
  .stat--likes { left: 345px; top: 410px; }

  .stats-band {
    position: absolute; left: 360px; top: 282px; width: 190px; height: 28px;
    background: var(--grey-dark); color: #fff; font-weight: 700; font-size: 10.5px;
    display: flex; align-items: center; padding-left: 30px;
  }
  .stats-badge {
    position: absolute; left: 328px; top: 279px; width: 38px; height: 34px;
    background: var(--orange); border-radius: 4px;
    display: flex; align-items: center; justify-content: center;
  }
  .stats-badge span { width: 17px; height: 17px; background: #fff; border-radius: 3px; }

  /* Right page */
  .event-visual { position: absolute; left: 20px; top: 20px; width: 260px; height: 340px; }
  .partners { position: absolute; right: 40px; width: 330px; text-align: right; }
  .partners h4 { font-size: 10px; font-weight: 700; color: var(--ink); margin-bottom: 6px; }
  .partners hr { border: 0; border-top: 1px solid var(--rule); margin-bottom: 10px; }
  .partners--previous { top: 160px; }
  .partners--international { top: 300px; }
  .logo-row { display: flex; justify-content: flex-end; align-items: center; gap: 9px; margin-bottom: 10px; }
  .partner-name { font-family: "Arimo", sans-serif; font-weight: 700; font-size: 12px; color: var(--ink); white-space: nowrap; }
  .partner-mark { display: inline-block; width: 18px; height: 18px; background: var(--grey); }
  .partner-mark--round { border-radius: 50%; }
  .partner-mark--orange { background: var(--orange); }
  .partner-mark--dark { background: var(--ink); }
</style>
</head>
<body>
  <main class="spread">
    <section class="page page--left">
      <span class="folio-tab"></span>
      <h2 class="section-title">MARKETING</h2>

      <div class="copy-column">
        <div class="copy">
          <h3>Social Media</h3>
          <p>With over 30,000 visitors and 10,000 participants, Keel-Marrow events are the perfect opportunity to take advantage of Social Media as it’s the leading marketing tool in the industry. Take advantage of audience by engaging them in competitions and marketing campaigns.</p>
        </div>
        <div class="copy">
          <h3>Branding</h3>
          <p>In addition to CSR benefits - companies will be mentioned in all communications and branding outlets will be prominently displayed on location and media distributions.</p>
        </div>
      </div>

      <div class="stat stat--impressions"><span class="stat-figure">11.4<small>MILLION</small></span>Impressions during our<br>Events (Public Photos)</div>
      <div class="stat stat--comments"><span class="stat-figure">9,490<sup>+</sup></span>Comments during our<br>Events (Public Photos)</div>

      <div class="stats-band">Photoloop Statistics</div>
      <div class="stats-badge"><span></span></div>

      <div class="stat stat--contributors"><span class="stat-figure">476<sup>+</sup></span>Unique Contributors during<br>our Events (Public Photos)</div>
      <div class="stat stat--posts"><span class="stat-figure">1,000<sup>+</sup></span>Posts during our<br>Events (Public Photos)</div>
      <div class="stat stat--likes"><span class="stat-figure">81.25<small>%</small></span>Likes generated during our<br>Events (Public Photos)</div>
    </section>

    <section class="page page--right">
      <span class="folio-tab"></span>
      <svg class="event-visual" viewBox="0 0 260 340">
        <polygon points="10,200 70,60 70,200" fill="#8c8c90"/>
        <polygon points="60,50 250,0 250,20 60,70" fill="var(--orange)"/>
        <polygon points="30,340 75,200 100,200 55,340" fill="var(--orange)"/>
        <defs>
          <linearGradient id="kartGrad" x1="0" y1="0" x2="1" y2="1">
            <stop offset="0" stop-color="#c2663a"/>
            <stop offset=".5" stop-color="#7a4a35"/>
            <stop offset="1" stop-color="#c9b8a4"/>
          </linearGradient>
        </defs>
        <polygon role="img" aria-label="Photo of karting event pit lane with racers and crew" points="70,40 240,15 210,230 70,290" fill="url(#kartGrad)"/>
      </svg>

      <div class="partners partners--previous">
        <h4>Our Previous Partners</h4>
        <hr>
        <div class="logo-row">
          <span class="partner-name">Marlo</span>
          <span class="partner-name">Tallhorn</span>
          <span class="partner-mark partner-mark--round"></span>
        </div>
        <div class="logo-row">
          <span class="partner-name">Ridgeline</span>
          <span class="partner-name">Vantro</span>
          <span class="partner-name">Orbis</span>
          <span class="partner-mark partner-mark--dark"></span>
          <span class="partner-name">Crestfield</span>
          <span class="partner-name">Lapwise</span>
        </div>
        <div class="logo-row">
          <span class="partner-mark"></span>
          <span class="partner-mark partner-mark--orange"></span>
          <span class="partner-mark partner-mark--round"></span>
          <span class="partner-mark"></span>
          <span class="partner-mark partner-mark--round"></span>
          <span class="partner-mark"></span>
        </div>
      </div>

      <div class="partners partners--international">
        <h4>International Partners</h4>
        <hr>
        <div class="logo-row">
          <span class="partner-name">Fairmond</span>
          <span class="partner-name">Splitmark</span>
          <span class="partner-mark partner-mark--dark"></span>
          <span class="partner-name">Stridewell</span>
        </div>
      </div>
    </section>
  </main>
</body>
</html>
```